Australian Software Consultancy needs new Business Card Design

Design Business Card based on existing design artefacts (attached). We are open to all designs. As its a 2 sided design and we thought it might be quite striking to have one side with a black background and te other side with a white background.

Target Market(s)

Financial Services mainly.

Industry/Entity Type

Business

Contact Information for Business Card

Name :
Position :
Email :

Requirements
Must have
• Funky design using our existing assets

```html
<!DOCTYPE html>
<html lang="en">
<head>
<meta charset="utf-8">
<title>Clearsight Business Card</title>
<link rel="stylesheet" href="https://fonts.googleapis.com/css2?family=Montserrat:wght@600&family=Open+Sans:wght@400;600;700&display=swap">
<style>
  :root {
    --page: #ecebe8;
    --ink: #1f1f1f;
    --card-dark: #262626;
    --card-light: #ffffff;
    --accent: #e1252b;
    --muted: #e4e4e4;
    --text-dark: #1a1a1a;
    --text-grey: #444444;
  }
  html, body {
    margin: 0;
    width: 1200px;
    height: 800px;
    overflow: hidden;
    background: var(--page);
  }
  .canvas {
    position: relative;
    width: 1200px;
    height: 800px;
  }
  .card {
    position: absolute;
    top: 245px;
    width: 540px;
    height: 310px;
    border-radius: 18px;
    overflow: hidden;
    box-shadow: 0 10px 30px rgba(0,0,0,0.18);
  }
  .card--back {
    left: 40px;
    background: var(--card-dark);
  }
  .card--front {
    left: 620px;
    background: var(--card-light);
  }
  .brand-lockup {
    position: absolute;
    left: 0; right: 0; top: 0; bottom: 0;
    display: flex;
    align-items: center;
    justify-content: center;
    gap: 18px;
  }
  .brand-mark {
    width: 64px;
    height: 64px;
    border: 5px solid var(--accent);
    border-radius: 50%;
    box-sizing: border-box;
  }
  .brand-name {
    font-family: "Montserrat", sans-serif;
    font-weight: 600;
    letter-spacing: 2px;
    color: var(--accent);
    font-size: 38px;
  }
  .front-art {
    position: absolute;
    inset: 0;
  }
  .front-brand {
    position: absolute;
    left: 150px;
    top: 34px;
    font-family: "Montserrat", sans-serif;
    font-weight: 600;
    font-size: 24px;
    letter-spacing: 1px;
    color: var(--ink);
  }
  .identity {
    position: absolute;
    left: 0;
    top: 118px;
    padding-left: 26px;
    border-left: 10px solid var(--accent);
    font-family: "Open Sans", sans-serif;
  }
  .identity__name {
    margin: 0;
    font-size: 26px;
    font-weight: 400;
    color: var(--text-grey);
    line-height: 1.1;
  }
  .identity__name strong {
    font-weight: 700;
    color: var(--text-dark);
  }
  .identity__title {
    margin: 2px 0 0;
    font-size: 13px;
    color: var(--accent);
  }
  .contact {
    position: absolute;
    left: 36px;
    bottom: 30px;
    margin: 0;
    padding: 0;
    list-style: none;
    font-family: "Open Sans", sans-serif;
    font-size: 13px;
    color: var(--text-grey);
  }
  .contact li {
    display: flex;
    align-items: center;
    gap: 8px;
    margin-top: 6px;
  }
  .contact svg {
    width: 14px;
    height: 14px;
    fill: var(--accent);
  }
</style>
</head>
<body>
<main class="canvas">
  <section class="card card--back" aria-label="Card back">
    <div class="brand-lockup">
      <div class="brand-mark"></div>
      <span class="brand-name">CLEARSIGHT</span>
    </div>
  </section>

  <section class="card card--front" aria-label="Card front">
    <svg class="front-art" viewBox="0 0 540 310" aria-hidden="true">
      <rect x="0" y="0" width="540" height="310" fill="var(--card-dark)"/>
      <path d="M0 0 H430 C470 0 470 40 455 80 C430 150 430 200 460 250 C480 285 470 310 440 310 H0 Z"
            fill="var(--card-light)"/>
      <path d="M430 0 C478 0 478 42 462 82 C438 150 438 200 468 250 C488 285 478 310 446 310"
            fill="none" stroke="var(--card-light)" stroke-width="14"/>
      <path d="M432 4 C470 4 470 42 454 80 C430 150 430 200 460 250 C478 282 470 306 442 306"
            fill="none" stroke="var(--accent)" stroke-width="4"/>
      <circle cx="340" cy="140" r="100" fill="none" stroke="var(--muted)" stroke-width="12"/>
    </svg>
    <div class="front-brand">CLEARSIGHT</div>
    <div class="identity">
      <h1 class="identity__name">Your <strong>Name</strong></h1>
      <p class="identity__title">Job Title</p>
    </div>
    <ul class="contact">
      <li>
        <svg viewBox="0 0 24 24"><path d="M6.6 10.8a15 15 0 0 0 6.6 6.6l2.2-2.2c.3-.3.7-.4 1-.2 1.1.4 2.3.6 3.6.6.6 0 1 .4 1 1V20c0 .6-.4 1-1 1C10.6 21 3 13.4 3 4c0-.6.4-1 1-1h3.5c.6 0 1 .4 1 1 0 1.3.2 2.5.6 3.6.1.3 0 .7-.2 1z"/></svg>
        000 000 0000
      </li>
      <li>
        <svg viewBox="0 0 24 24"><path d="M2 5h20v14H2z M2 5l10 7 10-7" /></svg>
        youremail@xyz.com
      </li>
    </ul>
  </section>
</main>
</body>
</html>
```